Banner Ad Design Project for responsive website

Looking to update the main banner on my website www.vowlantern.example but it will be for our new responsive website, you can see here http://www.vowlantern.example/dev/
Banner should be 300 px high by1920 pix wide
Please contact me with any questions
Should include:
All the text from the existing banner ie
Bridal Show
THE FIRST 50 BRIDES WILL GET A CHANCE TO WIN $25000
Honeymoon Cruise Giveaway
"Pick Your Perfect Gown" casting call
Banner should be 1920 pix wide
Final delivery will require layered psd file and all fonts

Target Market(s)

Brides

Industry/Entity Type

Call

Requirements
Must have
• All the text from the existing banner ie
• Bridal Show
• THE FIRST 50 BRIDES WILL GET A CHANCE TO WIN $25000
• Honeymoon Cruise Giveaway
• "Pick Your Perfect Gown" casting call
• Banner should be 1920 pix wide
Nice to have
• The look and feel of our postcard, see attached
Should not have
• Any specifics to any date/time/location as the banner will be online all the time and the specifics for each show will be different

```html
<!DOCTYPE html>
<html lang="en">
<head>
<meta charset="utf-8">
<title>Bridal Show — Vow Lantern</title>
<link rel="stylesheet" href="https://fonts.googleapis.com/css2?family=Great+Vibes&family=PT+Sans:wght@400;700&display=swap">
<style>
  :root {
    --brand-blue: #2f6fa8;
    --text-grey: #4d4d4d;
    --rule-grey: #9a9a9a;
    --sky-blue: #4ba6e4;
    --pale-blue: #a9d6f3;
    --white: #ffffff;
    --photo-light: #f7f7f6;
    --photo-mid: #e4e3e1;
    --photo-warm: #eadbcf;
  }
  html, body {
    margin: 0;
    padding: 0;
    overflow: hidden;
    background: var(--white);
  }
  .banner {
    position: relative;
    width: 1920px;
    height: 300px;
    overflow: hidden;
    font-family: "PT Sans", Arial, sans-serif;
  }
  .hero-photo {
    position: absolute;
    inset: 0;
    background:
      radial-gradient(ellipse 340px 170px at 1520px 110px, var(--photo-warm), transparent 72%),
      linear-gradient(95deg, var(--photo-light) 0%, var(--photo-light) 55%, var(--photo-mid) 80%, #d8d7d4 100%);
  }
  .headline {
    position: absolute;
    left: 40px;
    top: 0;
    margin: 0;
    font-family: "Great Vibes", cursive;
    font-weight: 400;
    font-size: 96px;
    line-height: 115px;
    color: var(--brand-blue);
    white-space: nowrap;
  }
  .casting-call {
    position: absolute;
    left: 96px;
    top: 116px;
    margin: 0;
    font-size: 26px;
    line-height: 32px;
    color: var(--text-grey);
    text-transform: uppercase;
    white-space: nowrap;
  }
  .casting-call .script {
    font-family: "Great Vibes", cursive;
    text-transform: none;
    color: var(--brand-blue);
    font-size: 34px;
  }
  .rule {
    position: absolute;
    left: 620px;
    width: 500px;
    border-top: 2px dashed var(--rule-grey);
  }
  .rule--top { top: 22px; }
  .rule--bottom { top: 92px; }
  .prize-lead {
    position: absolute;
    left: 620px;
    width: 300px;
    top: 36px;
    margin: 0;
    text-align: right;
    font-weight: 700;
    font-size: 18px;
    line-height: 21px;
    color: var(--text-grey);
    text-transform: uppercase;
    white-space: nowrap;
  }
  .prize-amount {
    position: absolute;
    left: 935px;
    top: 30px;
    margin: 0;
    font-weight: 700;
    font-size: 44px;
    line-height: 54px;
    color: var(--brand-blue);
    white-space: nowrap;
  }
  .cruise-photo {
    position: absolute;
    left: 620px;
    top: 108px;
    width: 210px;
    height: 90px;
    background: linear-gradient(180deg, #7fc3ec 0%, #b9e0f5 45%, #f2f4f6 62%, #2f86c7 78%, #1f6aa8 100%);
  }
  .giveaway {
    position: absolute;
    left: 846px;
    top: 104px;
    margin: 0;
    font-family: "Great Vibes", cursive;
    font-weight: 400;
    font-size: 34px;
    line-height: 36px;
    color: var(--brand-blue);
    white-space: nowrap;
  }
  .admission {
    position: absolute;
    left: 848px;
    top: 178px;
    margin: 0;
    font-size: 15px;
    line-height: 18px;
    color: var(--text-grey);
    text-transform: uppercase;
  }
  .footer-wave {
    position: absolute;
    left: 0;
    top: 0;
    width: 1920px;
    height: 300px;
  }
  .brand-name {
    position: absolute;
    left: 40px;
    top: 254px;
    margin: 0;
    font-size: 28px;
    line-height: 32px;
    font-weight: 400;
    color: var(--white);
    text-transform: uppercase;
    letter-spacing: 1px;
  }
  .cta-button {
    position: absolute;
    left: 1640px;
    top: 234px;
    width: 240px;
    height: 50px;
    box-sizing: border-box;
    border: 2px solid var(--white);
    display: flex;
    align-items: center;
    justify-content: center;
    gap: 10px;
    color: var(--white);
    text-decoration: none;
    font-size: 21px;
    text-transform: uppercase;
    letter-spacing: 1px;
  }
  .cta-button svg { width: 14px; height: 17px; }
</style>
</head>
<body>
<main class="banner">
  <div class="hero-photo" role="img" aria-label="Photograph of a smiling bride in a lace wedding gown lying on a white floor, holding a bouquet of white roses"></div>

  <svg class="footer-wave" viewBox="0 0 1920 300" preserveAspectRatio="none" aria-hidden="true">
    <path d="M0 226 C 450 196, 850 200, 1250 214 C 1550 222, 1760 196, 1920 176 L1920 300 L0 300 Z" fill="var(--pale-blue)"/>
    <path d="M0 244 C 450 216, 850 220, 1250 232 C 1550 240, 1760 214, 1920 196 L1920 300 L0 300 Z" fill="var(--sky-blue)"/>
  </svg>

  <h1 class="headline">Bridal Show</h1>
  <p class="casting-call">Open casting call<br>Pick Your <span class="script">Perfect</span> Gown</p>

  <div class="rule rule--top"></div>
  <p class="prize-lead">The first 50 brides will<br>get a chance to win</p>
  <p class="prize-amount">$25 000</p>
  <div class="rule rule--bottom"></div>

  <div class="cruise-photo" role="img" aria-label="Photograph of a white cruise ship sailing on a blue sea"></div>
  <h2 class="giveaway">Honeymoon Cruise<br>Giveaway</h2>
  <p class="admission">$8 Admission</p>

  <p class="brand-name">Vow Lantern</p>

  <a class="cta-button" href="http://www.vowlantern.example/dev/">
    Find out more
    <svg viewBox="0 0 14 17" aria-hidden="true"><path d="M1 1 L13 8.5 L1 16 Z" fill="var(--white)"/></svg>
  </a>
</main>
</body>
</html>
```